Postcard double sided

Title: DWIGHT'S REVENGE

Why would Dwight Kersting align himself with Gordon Tasker?

(photo of two guys)

Dwight approached elected officials that he wanted to run for office, but did not have money to finance his campaign. He wanted other elected officials to finance his campaign. Everyone told him that they would help him get the vote out, but that he needed to finance his own race.

In comes Gordon Tasker.

Gordon Tasker who has a pay to play scheme over at the City, told Dwight he would finance his campaign on one condition.

He needed to run against Stuart Hobbs.

Why would Dwight want to run with no money?

Backside

DWIGHT'S REVENGE

Dwight decided to run because no one on the school board would terminate Dwight's ex and her new boyfriend who both work for the school district. His ex even filed criminal charges against him that are still pending.

Mug Shot facing left (name the charges Criminal Trespass , and Criminal Mischief (highlight bold letters use two lines) mug shot facing right

Complaint one (then photo with full face) Compliant 2)
(showcharges)

Dwight's ultimate goal is to terminate his ex and her new boyfriend if elected.
Plus Gordon Tasker needs the majority on the school board to do what he does bet.

Kickbacks for Contracts.

They will hire their own contractors!
Say "No" to Dwight's Revenge and Gordon Tasker Money Grab!

Title On Back: all caps: DOMESTIC VIOLENCE

```html
<!DOCTYPE html>
<html lang="en">
<head>
<meta charset="utf-8">
<title>Dwight's Revenge – Postcard</title>
<link href="https://fonts.googleapis.com/css2?family=Anton&family=Roboto:wght@400;700&display=swap" rel="stylesheet">
<style>
  :root {
    --red: #ac0610;
    --dark: #1c1b20;
    --white: #ffffff;
    --ink: #333338;
    --heading-ink: #1a1a1a;
    --backdrop: #9b9b9b;
    --photo-a: #c9b7a6;
    --photo-b: #2f2f34;
  }
  * { box-sizing: border-box; margin: 0; padding: 0; }
  html, body { width: 848px; height: 1200px; overflow: hidden; }
  body { background: var(--backdrop); position: relative; font-family: 'Roboto', Arial, sans-serif; }

  .card { position: absolute; left: 27px; width: 791px; background: var(--white); overflow: hidden; }
  .card--front { top: 30px; height: 553px; }
  .card--back { top: 612px; height: 554px; }
  .card__shapes { position: absolute; inset: 0; width: 100%; height: 100%; }

  .title { position: absolute; font-family: 'Anton', Impact, sans-serif; font-weight: 400; letter-spacing: 0.5px; line-height: 1; }
  .title--front { left: 33px; top: 24px; font-size: 46px; color: var(--white); }
  .title--back { left: 23px; top: 28px; font-size: 35px; color: var(--red); }

  .duo-photo {
    position: absolute; left: 14px; top: 99px; width: 366px; height: 366px; border-radius: 50%;
    background: radial-gradient(circle at 50% 40%, var(--photo-a) 0%, #8d7f74 35%, var(--photo-b) 75%);
    border: 6px solid var(--white); box-shadow: 0 6px 14px rgba(0,0,0,.35);
  }

  .story { position: absolute; right: 18px; width: 330px; text-align: right; }
  .story__head { font-weight: 700; font-size: 19px; line-height: 24px; color: var(--red); }
  .story__head strong { color: var(--heading-ink); font-weight: 700; }
  .story__body { font-size: 14px; line-height: 20.5px; color: var(--ink); }

  .copy { position: absolute; left: 23px; font-size: 14px; line-height: 20.5px; color: var(--ink); }
  .copy--lead { top: 80px; width: 300px; }
  .copy--goal { top: 192px; width: 200px; }
  .copy--board { top: 270px; width: 235px; }
  .copy--hire { top: 372px; }
  .kicker { position: absolute; left: 23px; top: 338px; font-size: 19px; font-weight: 700; color: var(--heading-ink); }
  .kicker span, .closer__red { color: var(--red); }
  .closer { position: absolute; left: 23px; font-size: 17px; font-weight: 700; color: var(--heading-ink); white-space: nowrap; }
  .closer--one { top: 424px; }
  .closer--two { top: 451px; }

  .mugshot {
    position: absolute; width: 120px; height: 120px; border-radius: 50%;
    background: radial-gradient(circle at 50% 45%, #c49a80 0%, #e8e4e0 55%, #f4f4f4 100%);
    border: 3px solid var(--white); box-shadow: 0 3px 8px rgba(0,0,0,.3);
  }
  .mugshot--left { left: 350px; top: 54px; }
  .mugshot--right { left: 352px; top: 226px; }
  .mugshot--front { left: 314px; top: 407px; }

  .charge { position: absolute; width: 120px; text-align: center; font-weight: 700; font-size: 15px; line-height: 17px; color: var(--heading-ink); }
  .charge span { color: var(--red); display: block; }
  .charge--trespass { left: 352px; top: 180px; }
  .charge--mischief { left: 348px; top: 354px; }

  .complaint {
    position: absolute; background: var(--white); border: 1.5px solid #8c8c8c;
    padding: 5px 5px; box-shadow: 1px 2px 5px rgba(0,0,0,.35);
  }
  .complaint--one { left: 466px; top: 336px; width: 98px; height: 128px; }
  .complaint--two { left: 507px; top: 386px; width: 90px; height: 116px; }
  .complaint__title { font-size: 4px; font-weight: 700; color: #222; margin-bottom: 3px; letter-spacing: .2px; }
  .complaint__line { height: 1.2px; background: #777; margin-bottom: 2.4px; }
  .complaint__line--short { width: 55%; }
  .complaint__sign { height: 1px; background: #333; width: 45%; margin: 9px 0 3px auto; }

  .stamp-box { position: absolute; left: 669px; top: 48px; width: 79px; height: 79px; border: 1px solid #e0e0e0; }
  .address-line { position: absolute; left: 526px; width: 222px; border-top: 1px dashed #d5d5d5; }
</style>
</head>
<body>

<section class="card card--front">
  <svg class="card__shapes" viewBox="0 0 1513 1058" preserveAspectRatio="none" aria-hidden="true">
    <path d="M0 0 H1030 C820 100 640 300 660 560 C680 800 760 960 830 1058 H0 Z" fill="var(--red)"/>
    <path d="M1030 0 C820 100 640 300 660 560" fill="none" stroke="var(--dark)" stroke-width="14"/>
    <path d="M230 1058 C420 950 580 860 665 690 C690 850 760 980 830 1058 Z" fill="var(--dark)"/>
  </svg>

  <h1 class="title title--front">DWIGHT'S REVENGE</h1>
  <div class="duo-photo" role="img" aria-label="Photo of Dwight Kersting and Gordon Tasker standing together in suits"></div>

  <div class="story" style="top:43px">
    <h2 class="story__head">Why would Dwight Kersting<br>align himself with<br><strong>Gordon Tasker?</strong></h2>
  </div>
  <p class="story story__body" style="top:124px;width:285px">Dwight approached elected officials that he wanted to run for office, but did not have money to finance his campaign. He wanted other elected officials to finance his campaign. Everyone told him that they would help him get the vote out, but that he needed to finance his own race.</p>
  <div class="story" style="top:299px">
    <h2 class="story__head">In comes<br><strong>Gordon Tasker.</strong></h2>
  </div>
  <p class="story story__body" style="top:356px;width:310px">Gordon Tasker who has a pay to play scheme over at the City, told Dwight he would finance his campaign on one condition.</p>
  <div class="story" style="top:427px">
    <h2 class="story__head">He needed to run<br><strong>against Stuart Hobbs.</strong></h2>
  </div>
  <p class="story story__body" style="top:487px">Why would Dwight want to run with no money?</p>
</section>

<section class="card card--back">
  <svg class="card__shapes" viewBox="0 0 791 554" preserveAspectRatio="none" aria-hidden="true">
    <path d="M287 0 H791 V554 H386 C470 480 520 380 500 260 C480 140 400 50 287 0 Z" fill="var(--red)"/>
    <path d="M349 0 H791 V546 C690 525 575 480 530 400 C515 300 495 130 349 0 Z" fill="var(--dark)"/>
    <path d="M700 554 C740 550 770 548 791 546 V554 Z" fill="var(--white)"/>
  </svg>

  <h1 class="title title--back">DOMESTIC VIOLENCE</h1>

  <p class="copy copy--lead">Dwight decided to run because no one on the school board would terminate Dwight's ex and her new boyfriend who both work for the school district. His ex even filed criminal charges against him that are still pending.</p>
  <p class="copy copy--goal">Dwight's ultimate goal is to terminate his ex and her new boyfriend if elected.</p>
  <p class="copy copy--board">Plus Gordon Tasker needs the majority on the school board to do what he does bet.</p>
  <p class="kicker"><span>Kickbacks</span> for Contracts.</p>
  <p class="copy copy--hire">They will hire their own contractors!</p>
  <p class="closer closer--one"><span class="closer__red">Say "No" to Dwight's Revenge</span></p>
  <p class="closer closer--two">and Gordon Tasker Money Grab!</p>

  <div class="mugshot mugshot--left" role="img" aria-label="Booking photo, profile facing right"></div>
  <p class="charge charge--trespass">Criminal <span>Trespass</span></p>
  <div class="mugshot mugshot--right" role="img" aria-label="Booking photo, profile facing left"></div>
  <p class="charge charge--mischief">Criminal <span>Mischief</span></p>
  <div class="mugshot mugshot--front" role="img" aria-label="Booking photo, full face"></div>

  <div class="complaint complaint--one">
    <p class="complaint__title">COMPLAINT NO. 1</p>
    <div class="complaint__line"></div><div class="complaint__line"></div><div class="complaint__line"></div>
    <div class="complaint__line complaint__line--short"></div>
    <div class="complaint__line"></div><div class="complaint__line"></div><div class="complaint__line"></div>
    <div class="complaint__line complaint__line--short"></div>
    <div class="complaint__sign"></div>
    <div class="complaint__line"></div><div class="complaint__line complaint__line--short"></div>
  </div>
  <div class="complaint complaint--two">
    <p class="complaint__title">COMPLAINT NO. 2</p>
    <div class="complaint__line"></div><div class="complaint__line"></div><div class="complaint__line"></div>
    <div class="complaint__line complaint__line--short"></div>
    <div class="complaint__line"></div><div class="complaint__line"></div><div class="complaint__line"></div>
    <div class="complaint__line complaint__line--short"></div>
    <div class="complaint__sign"></div>
    <div class="complaint__line"></div><div class="complaint__line complaint__line--short"></div>
  </div>

  <div class="stamp-box"></div>
  <div class="address-line" style="top:166px"></div>
  <div class="address-line" style="top:198px"></div>
  <div class="address-line" style="top:229px"></div>
  <div class="address-line" style="top:260px"></div>
  <div class="address-line" style="top:292px"></div>
</section>

</body>
</html>
```